Tasman Curdworks Guild needs new business cards

We need new business cards designed and produced. We are likely to need other design work done for ads, flyers etc in future.

We would like to start with an initial business card.

The Tasman Curdworks Guild (TCG) is a membership-based not-for-profit organisation that looks after the interests of Australia's small to medium artisan cheesemakers, many of whom are also small-scale farmers. The design should be simple, using our logo, but also communicate our artisan cheese and small dairy farm focus.

The first card to be designed and produced is for me, Miriam Tolhurst. My details are:

Miriam Tolhurst
Secretary
Tasman Curdworks Guild (TCG)
http://www.curdworksguild.example
T +61452837190
E miriam.miriamtolhurst@mailbox.example

I have attached the TCG logo in jpg form. I have a higher resolution version available if needed.

Thank you!

Miriam

Miriam Tolhurst
Tasman Curdworks Guild
miriam.miriamtolhurst@mailbox.example
+61452837190

Sans Serif

• Logo (see attached file)

```html
<!DOCTYPE html>
<html lang="en">
<head>
<meta charset="utf-8">
<title>Tasman Curdworks Guild — Business Card</title>
<link rel="stylesheet" href="https://fonts.googleapis.com/css2?family=Roboto:wght@400;500;700&display=swap">
<style>
  :root {
    --backdrop: #2c2c2e;
    --card-white: #ffffff;
    --cheese-yellow: #fdd06a;
    --rind-brown: #5e3613;
    --ink: #3a2a1c;
    --muted: #6b6b6b;
  }
  * { box-sizing: border-box; margin: 0; padding: 0; }
  html, body {
    width: 1200px; height: 950px; overflow: hidden;
    background: var(--backdrop);
    font-family: "Roboto", Arial, sans-serif;
  }
  .stage { position: relative; width: 1200px; height: 950px; }
  .card {
    position: absolute; left: 250px; width: 700px; height: 400px;
    overflow: hidden; border-radius: 4px;
  }
  .card--front { top: 55px; background: var(--card-white); }
  .card--back { top: 495px; background: var(--cheese-yellow); }

  .org-mark { display: flex; align-items: center; gap: 22px; position: absolute; }
  .org-mark__dot { width: 74px; height: 74px; border-radius: 50%; flex: none; }
  .org-mark__name { font-weight: 400; line-height: 1.15; }

  .card--front .org-mark { left: 56px; top: 122px; }
  .card--front .org-mark__dot { background: var(--cheese-yellow); }
  .card--front .org-mark__name { color: var(--rind-brown); font-size: 28px; width: 210px; }

  .card--back .org-mark { left: 50%; top: 50%; transform: translate(-50%, -50%); gap: 28px; }
  .card--back .org-mark__dot { width: 96px; height: 96px; background: var(--rind-brown); }
  .card--back .org-mark__name { color: var(--rind-brown); font-size: 36px; width: 260px; }

  .contact { position: absolute; right: 44px; top: 92px; text-align: right; }
  .contact__name { font-size: 30px; font-weight: 700; color: var(--ink); }
  .contact__role { font-size: 18px; color: #e8b640; margin-top: 4px; }
  .contact__list { list-style: none; margin-top: 30px; }
  .contact__item {
    display: flex; justify-content: flex-end; align-items: center; gap: 10px;
    font-size: 15px; color: var(--muted); margin-top: 10px;
  }
  .contact__item svg { width: 18px; height: 18px; fill: var(--rind-brown); flex: none; }

  .web-tab {
    position: absolute; right: 0; bottom: 22px; width: 330px; height: 52px;
    background: var(--rind-brown); border-top-left-radius: 14px;
    display: flex; align-items: center; justify-content: center;
    color: #ffffff; font-size: 17px; letter-spacing: 2px;
  }
  .base-strip { position: absolute; left: 0; right: 0; bottom: 0; height: 22px; background: var(--cheese-yellow); }
</style>
</head>
<body>
<main class="stage">
  <section class="card card--front" aria-label="Business card front">
    <div class="org-mark">
      <span class="org-mark__dot"></span>
      <span class="org-mark__name">Tasman Curdworks Guild</span>
    </div>

    <div class="contact">
      <p class="contact__name">Miriam Tolhurst</p>
      <p class="contact__role">Secretary</p>
      <ul class="contact__list">
        <li class="contact__item">
          <span>+61452837190</span>
          <svg viewBox="0 0 24 24" aria-hidden="true"><path d="M6.6 10.8a15.2 15.2 0 0 0 6.6 6.6l2.2-2.2a1 1 0 0 1 1-.25 11.4 11.4 0 0 0 3.6.57 1 1 0 0 1 1 1V20a1 1 0 0 1-1 1A17 17 0 0 1 3 4a1 1 0 0 1 1-1h3.5a1 1 0 0 1 1 1c0 1.25.2 2.45.57 3.57a1 1 0 0 1-.25 1z"/></svg>
        </li>
        <li class="contact__item">
          <span>miriam.miriamtolhurst@mailbox.example</span>
          <svg viewBox="0 0 24 24" aria-hidden="true"><path d="M3 5h18a1 1 0 0 1 1 1v12a1 1 0 0 1-1 1H3a1 1 0 0 1-1-1V6a1 1 0 0 1 1-1zm9 7.5L20 7H4z"/></svg>
        </li>
      </ul>
    </div>

    <div class="web-tab">www.curdworksguild.example</div>
    <div class="base-strip"></div>
  </section>

  <section class="card card--back" aria-label="Business card back">
    <div class="org-mark">
      <span class="org-mark__dot"></span>
      <span class="org-mark__name">Tasman Curdworks Guild</span>
    </div>
  </section>
</main>
</body>
</html>
```